Business card for STEADYWAVE

Please design professional business card for IT consulting firm STEADYWAVE INC.
Use logo attached.
Use information from sample qNode business card attached.
replace qnode inc with STEADYWAVE INC.
as well as qnodeinc.com with steadywave.example

```html
<!DOCTYPE html>
<html lang="en">
<head>
<meta charset="utf-8">
<title>STEADYWAVE INC. — Business Card</title>
<link rel="stylesheet" href="https://fonts.googleapis.com/css2?family=Outfit:wght@300;400;600;700&display=swap">
<style>
  :root {
    --backdrop: #d6d6d6;
    --card-white: #ffffff;
    --card-black: #000000;
    --ink: #111111;
    --accent-purple: #6a35a8;
    --mark-square: #8a1fd8;
    --band-purple: #7a3fa0;
    --band-orange: #f39a1e;
    --band-yellow: #cfd37a;
    --band-cyan: #5cc6e8;
  }
  * { box-sizing: border-box; margin: 0; padding: 0; }
  html, body { width: 1200px; height: 846px; overflow: hidden; }
  body {
    background: var(--backdrop);
    font-family: "Outfit", sans-serif;
    position: relative;
  }
  .card {
    position: absolute;
    top: 258px;
    width: 520px;
    height: 330px;
    box-shadow: 0 10px 24px rgba(0,0,0,0.18);
  }
  .card--front { left: 50px; background: var(--card-white); color: var(--ink); }
  .card--back  { left: 630px; background: var(--card-black); }

  .wordmark {
    position: absolute;
    display: flex;
    align-items: flex-start;
    gap: 6px;
    font-weight: 700;
    letter-spacing: 0.06em;
    line-height: 1;
  }
  .wordmark__square { display: block; background: var(--mark-square); }
  .card--front .wordmark { left: 34px; top: 100px; font-size: 38px; color: var(--ink); }
  .card--front .wordmark__square { width: 11px; height: 11px; }
  .card--back .wordmark {
    left: 50%; top: 50%; transform: translate(-50%, -50%);
    font-size: 50px; color: var(--card-white);
  }
  .card--back .wordmark__square { width: 14px; height: 14px; }

  .person { position: absolute; left: 44px; top: 154px; }
  .person__role { font-size: 12px; font-weight: 300; letter-spacing: 0.02em; }
  .person__name {
    margin-top: 3px; font-size: 15px; font-weight: 700; color: var(--accent-purple);
  }
  .person__credential { font-size: 9px; margin-left: 2px; }

  .contact { position: absolute; top: 206px; font-size: 13px; line-height: 19px; font-weight: 300; }
  .contact--phones { left: 56px; }
  .contact--web { left: 276px; top: 186px; }
  .contact__label { font-weight: 700; color: var(--accent-purple); }
  .contact__url { font-weight: 700; color: var(--accent-purple); }

  .spectrum-band {
    position: absolute;
    left: 40px; right: 30px; top: 258px; height: 6px;
    background: linear-gradient(90deg,
      var(--band-purple) 0%, var(--band-orange) 18%, var(--band-yellow) 36%,
      var(--band-cyan) 58%, var(--band-yellow) 74%, var(--band-orange) 88%, var(--band-purple) 100%);
  }
  .address {
    position: absolute; left: 52px; top: 280px;
    font-size: 12.5px; font-weight: 300; letter-spacing: 0.01em;
  }
</style>
</head>
<body>
  <section class="card card--front" aria-label="Business card front">
    <div class="wordmark">STEADYWAVE<span class="wordmark__square"></span></div>

    <div class="person">
      <p class="person__role">GENERAL MANAGER</p>
      <p class="person__name">DANIEL MARSH,<span class="person__credential">P. ENG.</span></p>
    </div>

    <div class="contact contact--phones">
      <p><span class="contact__label">office:</span> (555) 014-2270 ext. 201</p>
      <p><span class="contact__label">mobile:</span> (555) 019-3481</p>
    </div>

    <div class="contact contact--web">
      <p><span class="contact__label">email:</span> dmarsh@steadywave.example</p>
      <p class="contact__url">www.steadywave.example</p>
    </div>

    <div class="spectrum-band"></div>

    <p class="address">1820 Harbourline Ave., Suite 101 Brookfield, Ontario, A1A 1A1, Canada</p>
  </section>

  <section class="card card--back" aria-label="Business card back">
    <div class="wordmark">STEADYWAVE<span class="wordmark__square"></span></div>
  </section>
</body>
</html>
```